Company Real Estate Site Needs A Face Lift

I need a new website for the recent company I formed: Voska Real Estate.
You can use my agent website WWW.PALMIROQ.COM to see the style/brand I already have. I will have areas for Searching for homes on IDX, etc.
I really like this site:
http://www.cranfeltmanorhomes.com/
I have attached my logo as well

Industry/Entity Type

Real Estate

Colors
0255a3
ffffff
cee9f5

```html
<!DOCTYPE html>
<html lang="en">
<head>
<meta charset="utf-8">
<title>Voska Real Estate</title>
<link rel="stylesheet" href="https://fonts.googleapis.com/css2?family=Roboto:wght@400;500;700&family=Roboto+Condensed:wght@700&family=Dosis:wght@500;600&display=swap">
<style>
  :root {
    --page-bg: #262626;
    --brand-blue: #0255a3;
    --brand-pale: #cee9f5;
    --white: #ffffff;
    --nav-active: #2196f3;
    --panel-shade: rgba(20, 20, 20, 0.38);
    --nav-shade: rgba(10, 14, 20, 0.78);
    --arrow-shade: rgba(20, 20, 20, 0.85);
  }
  * { margin: 0; padding: 0; box-sizing: border-box; }
  html, body { width: 1200px; height: 591px; overflow: hidden; }
  body {
    background: var(--page-bg);
    font-family: "Roboto", sans-serif;
    color: var(--white);
    position: relative;
  }
  .hero {
    position: absolute; left: 15px; top: 43px; width: 1170px; height: 539px;
    background:
      linear-gradient(180deg, #1f63c4 0%, #4a8de0 14%, #e8ecef 22%, #dfe3e2 40%, #6f8a52 56%, #3f6b35 66%, #2b8fd6 74%, #1aa0e0 88%, #c9b79a 100%);
  }
  .brand-tile {
    position: absolute; left: 140px; top: 0; width: 317px; height: 103px;
    background: var(--brand-pale);
    display: flex; align-items: center; justify-content: center; gap: 10px;
    z-index: 2;
  }
  .brand-mark { width: 14px; height: 14px; border-radius: 50%; background: var(--brand-blue); }
  .brand-name {
    font-family: "Roboto", sans-serif; font-weight: 700; font-size: 26px;
    color: var(--brand-blue); letter-spacing: 0.5px;
  }
  .social {
    position: absolute; top: 6px; left: 857px; display: flex; align-items: center;
    font-family: "Dosis", sans-serif; font-weight: 500; font-size: 21px; color: var(--white);
  }
  .social-label { margin-right: 18px; }
  .social-dot { width: 21px; height: 21px; background: var(--white); margin-right: 6px; }
  .intro {
    position: absolute; left: 168px; top: 146px; width: 890px; height: 324px;
    background: var(--panel-shade); padding: 30px 27px 0;
  }
  .agent-name { font-weight: 700; font-size: 51px; line-height: 1; letter-spacing: 1px; }
  .agent-phone { font-weight: 700; font-size: 26px; margin-top: 16px; }
  .agent-email { font-weight: 500; font-size: 20px; margin-top: 18px; }
  .intro-text {
    font-family: "Roboto Condensed", sans-serif; font-weight: 700; font-size: 13.5px;
    line-height: 26px; margin-top: 24px; width: 800px;
  }
  .slide-arrow {
    position: absolute; top: 251px; width: 74px; height: 74px; border-radius: 50%;
    background: var(--arrow-shade); border: 3px solid rgba(60,60,60,0.7);
  }
  .slide-arrow.prev { left: 38px; }
  .slide-arrow.next { left: 1087px; }
  .slide-arrow svg { position: absolute; left: 25px; top: 24px; }
  .main-nav {
    position: absolute; left: 135px; top: 518px; width: 926px; height: 64px;
    background: var(--nav-shade); display: flex; align-items: stretch; padding-left: 28px;
    font-family: "Dosis", sans-serif; font-weight: 600; font-size: 18.5px;
  }
  .nav-item { display: flex; align-items: center; padding: 0 18px; color: var(--white); }
  .nav-item.active { background: var(--nav-active); padding: 0 28px 0 47px; margin-right: 18px; }
</style>
</head>
<body>
  <div class="hero" role="img" aria-label="Photo of white Mediterranean villas with palm trees around a blue swimming pool with a steel ladder"></div>

  <div class="brand-tile">
    <span class="brand-mark"></span>
    <span class="brand-name">Voska Real Estate</span>
  </div>

  <div class="social">
    <span class="social-label">Follow Us:</span>
    <span class="social-dot"></span>
    <span class="social-dot"></span>
    <span class="social-dot"></span>
  </div>

  <div class="slide-arrow prev">
    <svg width="20" height="22" viewBox="0 0 20 22"><polyline points="14,1 4,11 14,21" fill="none" stroke="#ffffff" stroke-width="1.5"/></svg>
  </div>
  <div class="slide-arrow next">
    <svg width="20" height="22" viewBox="0 0 20 22"><polyline points="6,1 16,11 6,21" fill="none" stroke="#ffffff" stroke-width="1.5"/></svg>
  </div>

  <section class="intro">
    <h1 class="agent-name">CORIN VOSKA</h1>
    <p class="agent-phone">304-555-0147</p>
    <p class="agent-email">CorinVoska@hollowmail.com</p>
    <p class="intro-text">Whether you are a first time buyer, or a home buying expert, finding and purchasing your West Virginia dream home can be an overwhelming process. If you want to avoid the pitfalls and aggravation often accompanied with buying or selling a home, it may be in your best interest to work with a licensed agent. If you are considering buying or selling a home and would like to speak to a Charleston area Real Estate professional, call CORIN VOSKA 304-555-CORN (555-0147) or email corinvoska@hollowmail.com today.</p>
  </section>

  <nav class="main-nav">
    <span class="nav-item active">Home</span>
    <span class="nav-item">Search Homes</span>
    <span class="nav-item">Buy</span>
    <span class="nav-item">Sell</span>
    <span class="nav-item">Tours</span>
    <span class="nav-item">Testimonials</span>
    <span class="nav-item">Home Blog</span>
    <span class="nav-item">Contact Us</span>
  </nav>
</body>
</html>
```